Legal Stationary

A full set of stationery is required
The image and logo, along with colour, are set and attached.
The style should be modern, clean, and corporate. Not just a basic template off the web.
In addition to the address/website/email/phone fields for DX and KWT number, with the text “the firm is authorised and regulated by the KWT”
All files in all formats will be needed to allow editing after. Initial setup of templates will be required, and details for 4 business cards will be supplied.
Target Market(s)
Consumers of legal services
Industry/Entity Type
Legal

```html
<!DOCTYPE html>
<html lang="en">
<head>
<meta charset="utf-8">
<title>Halvern Law – Stationery Set</title>
<link rel="stylesheet" href="https://fonts.googleapis.com/css2?family=Montserrat:wght@400;500;600;700&family=Lato:wght@400;700&display=swap">
<style>
  :root{
    --brand-blue:#233a8c;
    --paper:#f4f4f5;
    --paper-shade:#e7e7e9;
    --ink:#1f1f24;
    --muted:#6b6b72;
    --backdrop:#d6d6d8;
    --white:#ffffff;
  }
  *{margin:0;padding:0;box-sizing:border-box}
  html,body{width:1200px;height:739px;overflow:hidden;background:var(--backdrop)}
  body{position:relative;font-family:"Lato",sans-serif;color:var(--ink)}
  .sheet{position:absolute;background:var(--paper);box-shadow:0 2px 5px rgba(0,0,0,.18);overflow:hidden}
  .abs{position:absolute}
  .wordmark{position:absolute;font-family:"Montserrat",sans-serif;font-weight:600;color:var(--brand-blue);letter-spacing:.02em;white-space:nowrap;line-height:1}
  .wordmark.on-blue{color:var(--white)}
  .contact{position:absolute;font-family:"Montserrat",sans-serif;color:var(--ink);white-space:nowrap}
  .contact li{list-style:none;display:flex;align-items:center}
  .contact svg{fill:var(--brand-blue);margin-right:.35em;flex:none}
  .address{position:absolute;font-family:"Montserrat",sans-serif;color:var(--ink);white-space:nowrap}
  .rule-v{position:absolute;width:.6px;background:var(--brand-blue)}
  .legal-line{position:absolute;left:0;right:0;text-align:center;font-family:"Montserrat",sans-serif;color:var(--ink);white-space:nowrap}

  /* business card */
  .card-front{left:46px;top:87px;width:154px;height:90px}
  .card-front .person{position:absolute;right:80px;top:48px;text-align:right;font-family:"Montserrat",sans-serif}
  .card-front .person-name{font-weight:700;color:var(--brand-blue);font-size:6.2px;letter-spacing:.03em}
  .card-front .person-role{font-size:4.3px;margin-top:1px}
  .card-back{left:211px;top:87px;width:154px;height:90px;background:var(--brand-blue)}

  /* email signature */
  .email-signature{left:387px;top:87px;width:296px;height:78px}
  .email-signature .person-name{position:absolute;left:137px;top:16px;font-family:"Montserrat",sans-serif;font-weight:700;color:var(--brand-blue);font-size:8.4px;letter-spacing:.02em}
  .email-signature .person-role{position:absolute;left:137px;top:28px;font-family:"Montserrat",sans-serif;font-size:5.2px}
  .portrait{position:absolute;left:241px;top:14px;width:50px;height:50px;border-radius:50%;border:1px solid var(--brand-blue);background:radial-gradient(circle at 50% 40%,#c9c9cc 0%,#8e9096 55%,#2c3245 100%)}

  /* letterhead */
  .letterhead{left:45px;top:209px;width:318px;height:452px}
  .letter-greeting{position:absolute;left:26px;top:117px;font-family:"Lato",sans-serif;font-weight:700;font-size:6.2px}
  .letter-role{position:absolute;left:26px;top:126px;font-weight:700;font-size:4.4px}
  .letter-date{position:absolute;right:28px;top:126px;font-size:4.5px;color:var(--muted)}
  .letter-body{position:absolute;left:26px;width:266px;top:151px;font-size:4.55px;line-height:7.75px;color:var(--muted);text-align:justify}
  .letter-body p{margin-bottom:7.7px}
  .signature-area{position:absolute;left:26px;top:326px;width:70px;height:18px;background:linear-gradient(90deg,rgba(31,31,36,.12),rgba(31,31,36,.04));border-radius:2px}

  /* compliments slip */
  .compliments{left:387px;top:192px;width:294px;height:151px}
  .compliments .slip-title{position:absolute;right:20px;top:22px;font-family:"Montserrat",sans-serif;color:var(--brand-blue);font-size:10px;font-weight:400}

  /* envelopes */
  .envelope-back{left:387px;top:357px;width:294px;height:145px;background:var(--white)}
  .envelope-front{left:387px;top:512px;width:294px;height:149px}

  /* presentation folder */
  .folder-outer{left:703px;top:48px;width:470px;height:294px;background:transparent;box-shadow:none;overflow:visible}
  .folder-cover{position:absolute;left:0;top:0;width:232px;height:294px;background:linear-gradient(120deg,#27409a,var(--brand-blue) 60%,#1f3480);box-shadow:0 2px 5px rgba(0,0,0,.2)}
  .folder-backpanel{position:absolute;left:232px;top:0;width:238px;height:294px;background:linear-gradient(90deg,#dcdcde,var(--paper) 20%);box-shadow:0 2px 5px rgba(0,0,0,.2)}
  .folder-cover .cover-rule{position:absolute;left:20px;right:20px;top:222px;height:.6px;background:var(--white);opacity:.85}
  .folder-cover .cover-address{position:absolute;left:20px;right:20px;top:212px;text-align:center;font-family:"Montserrat",sans-serif;font-size:4.6px;color:var(--white)}
  .folder-cover .cover-contact{position:absolute;left:20px;right:20px;top:227px;text-align:center;font-family:"Montserrat",sans-serif;font-size:4.4px;color:var(--white);display:flex;justify-content:center;gap:6px}

  .folder-inner{left:708px;top:358px;width:447px;height:304px;background:var(--paper-shade)}
  .folder-inner .inner-left{position:absolute;left:0;top:0;width:223px;height:304px;background:var(--paper)}
  .mini-letter{position:absolute;left:246px;top:19px;width:185px;height:210px;background:var(--paper);box-shadow:0 1px 3px rgba(0,0,0,.15)}
  .mini-letter .letter-body{left:16px;top:89px;width:154px;font-size:2.6px;line-height:4.5px}
  .mini-letter .letter-body p{margin-bottom:4.5px}
  .folder-pockets{position:absolute;left:0;top:0}
</style>
</head>
<body>

<svg width="0" height="0" style="position:absolute" aria-hidden="true">
  <defs>
    <symbol id="icon-phone" viewBox="0 0 10 10"><path d="M2.2 0.6 3.8 2.6 2.9 3.7C3.5 5 4.9 6.5 6.3 7.1L7.4 6.2 9.4 7.8 8.4 9.4C4.6 9.2 0.8 5.4 0.6 1.6Z"/></symbol>
    <symbol id="icon-mail" viewBox="0 0 10 10"><path d="M0.5 2h9v6h-9zM1.3 3 5 5.8 8.7 3v4.4H1.3z"/></symbol>
    <symbol id="icon-web" viewBox="0 0 10 10"><circle cx="5" cy="5" r="4.3"/><path d="M0.7 5h8.6M5 0.7c-2.2 2.4-2.2 6.2 0 8.6M5 0.7c2.2 2.4 2.2 6.2 0 8.6" stroke="#fff" stroke-width=".7" fill="none"/></symbol>
  </defs>
</svg>

<!-- Business card, front -->
<section class="sheet card-front">
  <div class="wordmark" style="left:0;right:0;text-align:center;top:17px;font-size:12px">HALVERN LAW</div>
  <div class="person">
    <div class="person-name">SAMUEL OKAFOR</div>
    <div class="person-role">Attorney At Law</div>
  </div>
  <div class="rule-v" style="left:79px;top:45px;height:20px"></div>
  <ul class="contact" style="left:84px;top:46px;font-size:4.3px;line-height:6.3px">
    <li><svg width="4" height="4"><use href="#icon-phone"/></svg>(555) 014-2870</li>
    <li><svg width="4" height="4"><use href="#icon-mail"/></svg>info@halvernlaw.com</li>
    <li><svg width="4" height="4"><use href="#icon-web"/></svg>www.halvernlaw.com</li>
  </ul>
  <div class="legal-line" style="top:78px;font-size:4.2px">The Atrium, 48 Quayside Road, Northbridge, NB4 2QT</div>
</section>

<!-- Business card, back -->
<section class="sheet card-back">
  <div class="wordmark on-blue" style="left:0;right:0;text-align:center;top:37px;font-size:15px">HALVERN LAW</div>
</section>

<!-- Email signature -->
<section class="sheet email-signature">
  <div class="wordmark" style="left:16px;top:33px;font-size:11.5px">HALVERN LAW</div>
  <div class="rule-v" style="left:125px;top:13px;height:52px"></div>
  <div class="person-name">PETER ALDANE</div>
  <div class="person-role">Founder &amp; CEO</div>
  <ul class="contact" style="left:137px;top:39px;font-size:5.9px;line-height:8px">
    <li><svg width="5" height="5"><use href="#icon-phone"/></svg>555-019-3362</li>
    <li><svg width="5" height="5"><use href="#icon-mail"/></svg>info@halvernlaw.com</li>
    <li><svg width="5" height="5"><use href="#icon-web"/></svg>www.halvernlaw.com</li>
  </ul>
  <div class="rule-v" style="left:225px;top:13px;height:52px"></div>
  <div class="portrait" role="img" aria-label="Portrait photograph of the firm's founder"></div>
</section>

<!-- Presentation folder, outside -->
<section class="sheet folder-outer">
  <div class="folder-cover">
    <div class="wordmark on-blue" style="left:0;right:0;text-align:center;top:188px;font-size:17px">HALVERN LAW</div>
    <div class="cover-address">The Atrium, 48 Quayside Road, Northbridge, NB4 2QT</div>
    <div class="cover-rule"></div>
    <div class="cover-contact"><span>(555) 014-2870</span><span>info@halvernlaw.com</span><span>www.halvernlaw.com</span></div>
  </div>
  <div class="folder-backpanel">
    <div class="wordmark" style="left:0;right:0;text-align:center;top:36px;font-size:18px">HALVERN LAW</div>
    <div class="legal-line" style="top:264px;font-size:4px">The firm is authorised and regulated by the KWT &nbsp;/&nbsp; DX No - 418207 &nbsp;/&nbsp; KWT No - 418207</div>
  </div>
</section>

<!-- Letterhead -->
<section class="sheet letterhead">
  <div class="wordmark" style="left:26px;top:30px;font-size:16px">HALVERN LAW</div>
  <div class="address" style="left:172px;top:26px;font-size:5.4px;line-height:7.6px">The Atrium<br>48 Quayside Road<br>Northbridge, NB4 2QT</div>
  <div class="rule-v" style="left:232px;top:26px;height:24px"></div>
  <ul class="contact" style="left:238px;top:26px;font-size:5.4px;line-height:7.6px">
    <li><svg width="5" height="5"><use href="#icon-phone"/></svg>(555) 014-2870</li>
    <li><svg width="5" height="5"><use href="#icon-mail"/></svg>info@halvernlaw.com</li>
    <li><svg width="5" height="5"><use href="#icon-web"/></svg>www.halvernlaw.com</li>
  </ul>
  <div class="letter-greeting">Dear. Mrs Clara Whitford</div>
  <div class="letter-role">Chief Director</div>
  <div class="letter-date">Date: 17-June-2025</div>
  <div class="letter-body">
    <p>Lorem ipsum dolor sit amet, consectetur adipiscing elit, sed do eiusmod tempor incididunt ut labore et dolore magna aliqua. Sollicitudin ac orci phasellus egestas tellus rutrum tellus. Euismod elementum nisi quis eleifend quam adipiscing vitae proin sagittis. Egestas sed tempus urna et pharetra pharetra. Quis blandit turpis cursus in hac habitasse. Sed velit dignissim sodales ut eu. Ac auctor augue mauris augue neque. In arcu cursus euismod quis viverra nibh cras pulvinar mattis. Libero justo laoreet sit amet. Felis eget nunc lobortis mattis aliquam faucibus purus in. Pulvinar etiam non quam lacus suspendisse faucibus. Odio tempor orci dapibus ultrices. Velit dignissim sodales ut eu sem integer vitae justo. Fermentum et sollicitudin ac orci phasellus egestas. Pharetra vel turpis nunc eget lorem dolor sed. Sed turpis tincidunt id aliquet risus feugiat in ante. Mus mauris vitae ultricies leo integer malesuada nunc vel. Rhoncus urna neque viverra justo nec ultrices dui. Ut placerat orci nulla pellentesque dignissim enim sit amet.</p>
    <p>Bibendum arcu vitae elementum curabitur vitae nunc. Nunc pulvinar sapien et ligula ullamcorper malesuada. At elementum eu facilisis sed. Erat pellentesque adipiscing commodo elit at imperdiet dui accumsan sit. Nunc scelerisque viverra mauris in aliquam sem fringilla. In vitae turpis massa sed. Volutpat ac tincidunt vitae semper quis lectus nulla at. Massa placerat duis ultricies lacus sed turpis. Dui vivamus arcu felis bibendum ut tristique et egestas. Blandit aliquam etiam erat velit scelerisque in dictum non consectetur. Id neque aliquam vestibulum morbi blandit cursus risus at. Sed egestas egestas fringilla phasellus faucibus scelerisque eleifend donec. Ornare quam viverra orci sagittis eu volutpat odio facilisis. Volutpat sed cras ornare arcu dui vivamus arcu. Interdum consectetur libero id faucibus nisl.</p>
    <p>Viverra mauris in aliquam sem. Mattis molestie a iaculis at erat pellentesque adipiscing commodo elit. Sit amet volutpat consequat mauris nunc. Aliquam nulla facilisi cras fermentum. Sed turpis tincidunt id aliquet risus feugiat. Augue neque gravida in fermentum et sollicitudin ac orci.</p>
  </div>
  <div class="signature-area" role="img" aria-label="Handwritten signature of the sender"></div>
  <div class="legal-line" style="top:435px;font-size:5.4px">The firm is authorised and regulated by the KWT &nbsp;/&nbsp; DX No - 418207 &nbsp;/&nbsp; KWT No - 418207</div>
</section>

<!-- Compliments slip -->
<section class="sheet compliments">
  <div class="wordmark" style="left:18px;top:25px;font-size:15px">HALVERN LAW</div>
  <div class="slip-title">With Compliments</div>
  <div class="address" style="left:18px;top:70px;font-size:5.2px;line-height:7.5px">The Atrium<br>48 Quayside Road<br>Northbridge, NB4 2QT</div>
  <ul class="contact" style="left:18px;top:97px;font-size:5.2px;line-height:7.5px">
    <li><svg width="5" height="5"><use href="#icon-phone"/></svg>(555) 014-2870</li>
    <li><svg width="5" height="5"><use href="#icon-mail"/></svg>info@halvernlaw.com</li>
    <li><svg width="5" height="5"><use href="#icon-web"/></svg>www.halvernlaw.com</li>
  </ul>
  <div class="legal-line" style="top:135px;font-size:4.8px">The firm is authorised and regulated by the KWT &nbsp;/&nbsp; DX No - 418207 &nbsp;/&nbsp; KWT No - 418207</div>
</section>

<!-- Envelope, back with flap -->
<section class="sheet envelope-back">
  <svg class="abs" style="left:0;top:0" width="294" height="50" aria-hidden="true">
    <path d="M0 0H294L290 33Q288 47 275 47H19Q6 47 4 33Z" fill="var(--brand-blue)"/>
  </svg>
  <div class="wordmark on-blue" style="left:0;right:0;text-align:center;top:17px;font-size:14px">HALVERN LAW</div>
</section>

<!-- Envelope, front -->
<section class="sheet envelope-front">
  <div class="wordmark" style="left:18px;top:22px;font-size:12.5px">HALVERN LAW</div
  ><div class="rule-v" style="left:124px;top:18px;height:21px"></div>
  <div class="address" style="left:130px;top:18px;font-size:5px;line-height:6.9px">The Atrium<br>48 Quayside Road<br>Northbridge, NB4 2QT</div>
  <div class="legal-line" style="top:135px;font-size:4.8px">The firm is authorised and regulated by the KWT &nbsp;/&nbsp; DX No - 418207 &nbsp;/&nbsp; KWT No - 418207</div>
</section>

<!-- Presentation folder, inside -->
<section class="sheet folder-inner">
  <div class="inner-left"></div>
  <div class="mini-letter">
    <div class="wordmark" style="left:16px;top:18px;font-size:8.5px">HALVERN LAW</div>
    <div class="address" style="left:101px;top:15px;font-size:3px;line-height:4.4px">The Atrium<br>48 Quayside Road<br>Northbridge, NB4 2QT</div>
    <div class="rule-v" style="left:136px;top:15px;height:13px"></div>
    <ul class="contact" style="left:139px;top:15px;font-size:3px;line-height:4.4px">
      <li><svg width="3" height="3"><use href="#icon-phone"/></svg>(555) 014-2870</li>
      <li><svg width="3" height="3"><use href="#icon-mail"/></svg>info@halvernlaw.com</li>
      <li><svg width="3" height="3"><use href="#icon-web"/></svg>www.halvernlaw.com</li>
    </ul>
    <div class="letter-greeting" style="left:16px;top:68px;font-size:3.6px">Dear. Mrs Clara Whitford</div>
    <div class="letter-role" style="left:16px;top:74px;font-size:2.6px">Chief Director</div>
    <div class="letter-date" style="right:16px;top:74px;font-size:2.6px">Date: 17-June-2025</div>
    <div class="letter-body">
      <p>Lorem ipsum dolor sit amet, consectetur adipiscing elit, sed do eiusmod tempor incididunt ut labore et dolore magna aliqua. Sollicitudin ac orci phasellus egestas tellus rutrum tellus. Euismod elementum nisi quis eleifend quam adipiscing vitae proin sagittis. Egestas sed tempus urna et pharetra pharetra. Quis blandit turpis cursus in hac habitasse. Sed velit dignissim sodales ut eu. Ac auctor augue mauris augue neque. In arcu cursus euismod quis viverra nibh cras pulvinar mattis. Libero justo laoreet sit amet. Felis eget nunc lobortis mattis aliquam faucibus purus in. Pulvinar etiam non quam lacus suspendisse faucibus. Odio tempor orci dapibus ultrices.</p>
      <p>Bibendum arcu vitae elementum curabitur vitae nunc. Nunc pulvinar sapien et ligula ullamcorper malesuada. At elementum eu facilisis sed. Erat pellentesque adipiscing commodo elit at imperdiet dui accumsan sit. Nunc scelerisque viverra mauris in aliquam sem fringilla. In vitae turpis massa sed. Volutpat ac tincidunt vitae semper quis lectus nulla at. Massa placerat duis ultricies lacus sed turpis.</p>
      <p>Viverra mauris in aliquam sem. Mattis molestie a iaculis at erat pellentesque adipiscing commodo elit. Sit amet volutpat consequat mauris nunc. Aliquam nulla facilisi cras fermentum.</p>
    </div>
    <div class="signature-area" style="left:16px;top:192px;width:40px;height:10px" role="img" aria-label="Handwritten signature of the sender"></div>
  </div>
  <svg class="folder-pockets" width="447" height="304" aria-hidden="true">
    <path d="M0 224H200Q206 224 208 230L222 304H0Z" fill="var(--brand-blue)"/>
    <path d="M224 304L238 230Q240 224 246 224H447V304Z" fill="var(--brand-blue)"/>
  </svg>
</section>

</body>
</html>
```